Bows Catalog Cover

Cover Page for a catalog for bows. Same logo MOR Morvane Alpina Cordaria.
Catalog overview: https://www.folioworks-demo.net/MOR-Morvane-Alpina-Cordaria/catalogs/MOR-catalog.html
No instruments, no scores, Only bows or bow parts (head, frog ...). Drawings or pictures.

Target Market(s)

Violin makers and reseller

Requirements
Must have
• bows or bow parts
Nice to have
• Drawings and or pictures
Should not have
• full Instruments or scores

```html
<!DOCTYPE html>
<html lang="en">
<head>
<meta charset="utf-8">
<title>MOR Morvane Alpina Cordaria – Catalog for Bows</title>
<link rel="stylesheet" href="https://fonts.googleapis.com/css2?family=Montserrat:wght@300;400;600&display=swap">
<style>
  :root {
    --paper: #f2f3f2;
    --paper-glow: #ffffff;
    --magenta: #9b2490;
    --indigo: #2e3192;
    --ink-grey: #6a6a6a;
    --hairline: #c9cbcb;
    --disc: #e9eaea;
    --disc-edge: #c8c8c8;
    --shadow: rgba(0, 0, 0, 0.18);
  }
  * { margin: 0; padding: 0; box-sizing: border-box; }
  html, body {
    width: 914px;
    height: 1200px;
    overflow: hidden;
    background: var(--paper);
  }
  .cover {
    position: relative;
    width: 914px;
    height: 1200px;
    overflow: hidden;
    background: radial-gradient(ellipse 55% 45% at 50% 55%, var(--paper-glow) 0%, var(--paper) 100%);
    font-family: "Montserrat", Arial, sans-serif;
  }
  .hairlines {
    position: absolute;
    inset: 0;
    width: 914px;
    height: 1200px;
  }
  .hairlines line {
    stroke: var(--hairline);
    stroke-width: 1;
  }

  /* brand */
  .brand {
    position: absolute;
    left: 84px;
    top: 104px;
    display: flex;
    align-items: center;
    gap: 22px;
  }
  .brand-dot {
    width: 88px;
    height: 88px;
    border-radius: 50%;
    background: var(--magenta);
  }
  .brand-text {
    color: var(--magenta);
    font-weight: 600;
  }
  .brand-name {
    display: block;
    font-size: 76px;
    line-height: 1;
    letter-spacing: 4px;
  }
  .brand-sub {
    display: block;
    margin-top: 8px;
    font-size: 11.5px;
    letter-spacing: 2.4px;
    text-transform: uppercase;
  }

  /* title */
  .title-kicker,
  .title-main {
    position: absolute;
    transform-origin: left top;
    transform: rotate(-90deg);
    white-space: nowrap;
  }
  .title-kicker {
    left: 327px;
    top: 846px;
    font-size: 36px;
    font-weight: 300;
    letter-spacing: 1px;
    color: var(--ink-grey);
    line-height: 1;
  }
  .title-main {
    left: 374px;
    top: 978px;
    font-size: 180px;
    font-weight: 400;
    line-height: 1;
    letter-spacing: 4px;
    background: linear-gradient(to bottom, var(--magenta) 20%, var(--indigo) 80%);
    -webkit-background-clip: text;
    background-clip: text;
    color: transparent;
  }

  /* product discs */
  .bow-disc {
    position: absolute;
    width: 160px;
    height: 190px;
  }
  .bow-disc svg { display: block; }
  .disc-1 { left: 573px; top: 427px; }
  .disc-2 { left: 578px; top: 608px; }
  .disc-3 { left: 582px; top: 807px; }

  .footer-band {
    position: absolute;
    left: 0;
    bottom: 0;
    width: 914px;
    height: 11px;
    background: linear-gradient(to right, var(--magenta), var(--indigo));
  }
</style>
</head>
<body>
<main class="cover">

  <svg class="hairlines" viewBox="0 0 914 1200" aria-hidden="true">
    <line x1="639" y1="310" x2="789" y2="172"/>
    <line x1="644" y1="354" x2="846" y2="166"/>
    <line x1="711" y1="339" x2="825" y2="232"/>
    <line x1="80"  y1="493" x2="230" y2="354"/>
    <line x1="85"  y1="536" x2="286" y2="349"/>
    <line x1="152" y1="521" x2="267" y2="415"/>
    <line x1="71"  y1="1114" x2="221" y2="975"/>
    <line x1="76"  y1="1157" x2="278" y2="970"/>
    <line x1="143" y1="1142" x2="258" y2="1036"/>
  </svg>

  <header class="brand">
    <span class="brand-dot" aria-hidden="true"></span>
    <span class="brand-text">
      <span class="brand-name">MOR</span>
      <span class="brand-sub">Morvane Alpina Cordaria</span>
    </span>
  </header>

  <h1>
    <span class="title-kicker">CATALOG FOR</span>
    <span class="title-main">BOWS</span>
  </h1>

  <figure class="bow-disc disc-1">
    <svg width="160" height="190" viewBox="0 0 160 190">
      <defs>
        <linearGradient id="arc-a" x1="0" y1="0" x2="1" y2="0">
          <stop offset="0" stop-color="#9b2490"/><stop offset="1" stop-color="#2e3192"/>
        </linearGradient>
      </defs>
      <ellipse cx="80" cy="164" rx="56" ry="4" fill="rgba(0,0,0,0.14)"/>
      <circle cx="80" cy="80" r="72" fill="none" stroke="#c8c8c8" stroke-width="1"/>
      <path d="M8 80 A72 72 0 0 0 152 80" fill="none" stroke="url(#arc-a)" stroke-width="3"/>
      <circle cx="80" cy="80" r="62" fill="#e9eaea" role="img" aria-label="Photo of violin bow heads and frogs"/>
    </svg>
  </figure>

  <figure class="bow-disc disc-2">
    <svg width="160" height="190" viewBox="0 0 160 190">
      <ellipse cx="80" cy="164" rx="56" ry="4" fill="rgba(0,0,0,0.14)"/>
      <circle cx="80" cy="80" r="72" fill="none" stroke="#c8c8c8" stroke-width="1"/>
      <path d="M8 80 A72 72 0 0 0 152 80" fill="none" stroke="url(#arc-a)" stroke-width="3"/>
      <circle cx="80" cy="80" r="62" fill="#e9eaea" role="img" aria-label="Photo of carbon bow heads and frogs"/>
    </svg>
  </figure>

  <figure class="bow-disc disc-3">
    <svg width="160" height="190" viewBox="0 0 160 190">
      <ellipse cx="80" cy="164" rx="56" ry="4" fill="rgba(0,0,0,0.14)"/>
      <circle cx="80" cy="80" r="72" fill="none" stroke="#c8c8c8" stroke-width="1"/>
      <path d="M8 80 A72 72 0 0 0 152 80" fill="none" stroke="url(#arc-a)" stroke-width="3"/>
      <circle cx="80" cy="80" r="62" fill="#e9eaea" role="img" aria-label="Photo of pernambuco bow heads and frogs"/>
    </svg>
  </figure>

  <div class="footer-band" aria-hidden="true"></div>
</main>
</body>
</html>
```